Flyer-Design für Open Workspace Lösung
Zielgruppe
Was machen wir? Open Workspace Lösung für Ärzte und Psychotherapeuten.
Zielgruppe: Unser Angebot richtet sich an Ärzte, Psychologen, Psychotherapeuten, Heilpraktiker für Psychotherapie (HeilprG) sowie Coaches und Supervisoren mit vergleichbarem und zertifiziertem Hintergrund. Darüber hinaus stehen die Räume auch für Seminare, Workshops oder Gruppenangebote zur Verfügung.
Aufgabenstellung
1. Die Word-Skizze ist ein Entwurf, der gerne verändert werden kann.
2. Das Foto in der oberen Hälfte ist ein Platzhalter. Es ist zwar real aber wir haben leider noch kein gutes Foto der fertigen Räume. Daher sollte, falls ein Bild verwendet wird, eine bearbeitbare Version mitgeliefert werden, damit wir das Bild noch austauschen können. Es muss kein Bild im Flyer verwendet werden, kann aber.
3. Unser Logo sollte auf den Flyer kommen. Es gibt das Logo mit und ohne Text. Beide hängen wir als Datei mit an.
4. Wir haben eine Website: www.praxis-sonnenwiese.de
Der Flyer sollte zu dieser passen. Die Schriftart der Website ist font-famliy: 'Lato', sans-serif und sollte verwendet werden.
5. Die Farbe (türkis) ist vorgegeben. Die Definition ist: #0CE0AE
Die Grautöne der Website sind folgende: #444444, #555444, #5A5A5A, #888888, #CCCCCC #F4F4F4
6. wir hätten gerne einen one-pager, den man als Werbung an Emails anhängen und im Internet veröffentlichen kann und einen Flyer, der ausgedruckt ausliegen kann

```html
<!DOCTYPE html>
<html lang="de">
<head>
<meta charset="utf-8">
<title>Praxis an der Sonnenwiese – Flyer</title>
<link href="https://fonts.googleapis.com/css2?family=Lato:wght@300;400;700&family=Raleway:wght@200;300&display=swap" rel="stylesheet">
<style>
:root{
  --turquoise:#0CE0AE;
  --turquoise-dark:#00503c;
  --grey-dark:#444444;
  --grey-text:#5A5A5A;
  --grey-line:#4a4a4a;
  --accent-text:#9c3d5e;
  --white:#ffffff;
}
*{margin:0;padding:0;box-sizing:border-box}
html,body{width:1200px;height:848px;overflow:hidden;background:var(--white)}
body{font-family:'Lato',sans-serif;color:var(--grey-text);position:relative}
.panel{position:absolute;top:0;height:848px;width:400px}
.panel-left{left:0;padding:80px 12px 0;text-align:center}
.panel-middle{left:400px;background:var(--turquoise);text-align:center;padding:80px 12px 0;color:var(--accent-text)}
.panel-right{left:800px}
h2{font-weight:700;font-size:19px;color:var(--grey-dark);letter-spacing:-.2px;margin-bottom:18px}
.copy{font-size:15px;line-height:16.1px;font-weight:400}
.copy p+p{margin-top:16px}
.left-sub{margin-top:20px;margin-bottom:18px;font-size:17px}
.chart-title{position:absolute;left:0;width:400px;top:566px;text-align:center;font-size:23px;color:var(--turquoise-dark);font-weight:400;letter-spacing:.5px;padding-left:30px}
.chart{position:absolute;left:10px;top:596px}
.middle-divider{width:166px;height:3px;background:var(--grey-line);margin:14px auto 16px}
.photo{position:absolute}
.photo-bottom{left:400px;top:627px;width:400px;height:188px;background:linear-gradient(135deg,#e7e2d8 0%,#cfc9bd 45%,#6b6e78 70%,#b9a384 100%)}
.photo-bottom-line{position:absolute;left:600px;top:625px;width:200px;height:3px;background:var(--grey-line)}
.brand{position:absolute;left:812px;top:30px;display:flex;align-items:center;gap:18px}
.brand-mark{width:58px;height:58px;background:#55c2a2}
.brand-name{font-family:'Raleway',sans-serif;font-weight:300;font-size:32px;line-height:30px;letter-spacing:4px;color:var(--grey-dark)}
.brand-line{position:absolute;left:800px;top:108px;width:72px;height:3px;background:var(--grey-line)}
.photo-top{left:800px;top:110px;width:400px;height:186px;background:linear-gradient(120deg,#8aa06a 0%,#e8e2cf 30%,#d9c96a 50%,#5b5d63 75%,#4c4e53 100%)}
.right-bar{position:absolute;left:846px;top:379px;width:354px;height:4px;background:var(--grey-line)}
.benefits{position:absolute;left:900px;top:383px;width:295px;height:465px;background:var(--turquoise);padding:4px 0 0 5px;color:var(--grey-dark);font-size:16.5px;line-height:16.5px}
.benefits .intro{margin-bottom:38px}
.benefit{position:absolute;left:870px;width:330px;height:61px;display:flex;align-items:flex-start}
.benefit-icon{width:61px;height:61px;background:var(--white);display:flex;align-items:center;justify-content:center;flex:none}
.benefit-text{padding:8px 0 0 7px;font-size:16.5px;line-height:16.5px;color:var(--grey-dark)}
</style>
</head>
<body>

<section class="panel panel-left">
  <h2>Preise der Therapieräume</h2>
  <div class="copy">
    <p>Die Therapieräume können in einem monatlichen Paket oder für einzelne Stunden gemietet werden. Dabei stehen sie Ihnen von Montag bis Sonntag zur Verfügung. Wenn Sie Interesse haben, nehmen Sie gerne mit uns Kontakt auf. Wir besichtigen die Räume und klären alle Fragen, gerne auch per Video. Wir vereinbaren einen Mietvertrag und dann können Sie jederzeit Räume buchen.</p>
    <p>Weitere Informationen finden Sie unter:<br>www.praxis-sonnenwiese.de</p>
  </div>
  <h2 class="left-sub">Monatliches Paket</h2>
  <div class="copy">
    <p>Unser Angebot zu besonders günstigen Konditionen: Sie legen fest, wie viele Stunden Sie pro Woche in unseren Räumen arbeiten möchten und können diese dann für einen attraktiven Stundensatz mieten. Die Höhe der Monatsmiete ergibt sich aus der Anzahl der gewählten Wochenstunden und dem Stundenpreis. Je mehr Stunden pro Woche Sie vereinbaren, desto günstiger wird der Mietpreis jeder einzelnen Stunde. Wählen Sie eine Stunde pro Woche, beträgt die Miete 17,-€/Stunde. Für jede weitere Stunde reduziert sich der Mietpreis aller Stunden um 0,50€. Ab 13 Stunden pro Woche gilt ein Mietpreis von 11€/Stunde.</p>
  </div>
</section>

<div class="chart-title">PREISSTAFFELUNG</div>
<svg class="chart" width="390" height="210" viewBox="0 0 390 210" font-family="Lato, sans-serif">
  <text x="28" y="10" font-size="7" fill="#444">[€]</text>
  <text x="20" y="125" font-size="13" fill="#00503c" transform="rotate(-90 20 125)" text-anchor="middle">Stundenpreis</text>
  <line x1="44" y1="20" x2="44" y2="133" stroke="#888" stroke-width=".8"/>
  <line x1="44" y1="133" x2="342" y2="133" stroke="#888" stroke-width=".8"/>
  <g font-size="7" fill="#444" text-anchor="end">
    <text x="38" y="23">20</text><text x="38" y="51">15</text><text x="38" y="79">10</text><text x="38" y="107">5</text>
  </g>
  <g stroke="#888" stroke-width=".6">
    <line x1="41" y1="21" x2="44" y2="21"/><line x1="41" y1="49" x2="44" y2="49"/><line x1="41" y1="77" x2="44" y2="77"/><line x1="41" y1="105" x2="44" y2="105"/>
  </g>
  <g id="bars" font-size="6.5" fill="#444" text-anchor="middle">
    <!-- each bar: base 133, 5.6px per unit, dark cap = 2 units -->
    <rect x="48" y="27.6" width="17" height="11.2" fill="#00503c"/><rect x="48" y="38.8" width="17" height="94.2" fill="var(--turquoise)"/><text x="56.5" y="46">17</text>
    <rect x="67.7" y="30.4" width="17" height="11.2" fill="#00503c"/><rect x="67.7" y="41.6" width="17" height="91.4" fill="var(--turquoise)"/><text x="76.2" y="49">16,5</text>
    <rect x="87.4" y="33.2" width="17" height="11.2" fill="#00503c"/><rect x="87.4" y="44.4" width="17" height="88.6" fill="var(--turquoise)"/><text x="95.9" y="52">16</text>
    <rect x="107.1" y="36" width="17" height="11.2" fill="#00503c"/><rect x="107.1" y="47.2" width="17" height="85.8" fill="var(--turquoise)"/><text x="115.6" y="55">15,5</text>
    <rect x="126.8" y="38.8" width="17" height="11.2" fill="#00503c"/><rect x="126.8" y="50" width="17" height="83" fill="var(--turquoise)"/><text x="135.3" y="57.5">15</text>
    <rect x="146.5" y="41.6" width="17" height="11.2" fill="#00503c"/><rect x="146.5" y="52.8" width="17" height="80.2" fill="var(--turquoise)"/><text x="155" y="60">14,5</text>
    <rect x="166.2" y="44.4" width="17" height="11.2" fill="#00503c"/><rect x="166.2" y="55.6" width="17" height="77.4" fill="var(--turquoise)"/><text x="174.7" y="63">14</text>
    <rect x="185.9" y="47.2" width="17" height="11.2" fill="#00503c"/><rect x="185.9" y="58.4" width="17" height="74.6" fill="var(--turquoise)"/><text x="194.4" y="66">13,5</text>
    <rect x="205.6" y="50" width="17" height="11.2" fill="#00503c"/><rect x="205.6" y="61.2" width="17" height="71.8" fill="var(--turquoise)"/><text x="214.1" y="68.5">13</text>
    <rect x="225.3" y="52.8" width="17" height="11.2" fill="#00503c"/><rect x="225.3" y="64" width="17" height="69" fill="var(--turquoise)"/><text x="233.8" y="71.5">12,5</text>
    <rect x="245" y="55.6" width="17" height="11.2" fill="#00503c"/><rect x="245" y="66.8" width="17" height="66.2" fill="var(--turquoise)"/><text x="253.5" y="74">12</text>
    <rect x="264.7" y="58.4" width="17" height="11.2" fill="#00503c"/><rect x="264.7" y="69.6" width="17" height="63.4" fill="var(--turquoise)"/><text x="273.2" y="77">11,5</text>
    <rect x="284.4" y="61.2" width="17" height="11.2" fill="#00503c"/><rect x="284.4" y="72.4" width="17" height="60.6" fill="var(--turquoise)"/><text x="292.9" y="80">11</text>
    <rect x="304.1" y="61.2" width="17" height="11.2" fill="#00503c"/><rect x="304.1" y="72.4" width="17" height="60.6" fill="var(--turquoise)"/><text x="312.6" y="80">11</text>
    <rect x="323.8" y="61.2" width="17" height="11.2" fill="#00503c"/><rect x="323.8" y="72.4" width="17" height="60.6" fill="var(--turquoise)"/><text x="332.3" y="80">11</text>
  </g>
  <g font-size="7" fill="#444" text-anchor="middle">
    <text x="56.5" y="146">1</text><text x="76.2" y="146">2</text><text x="95.9" y="146">3</text><text x="115.6" y="146">4</text><text x="135.3" y="146">5</text><text x="155" y="146">6</text><text x="174.7" y="146">7</text><text x="194.4" y="146">8</text><text x="214.1" y="146">9</text><text x="233.8" y="146">10</text><text x="253.5" y="146">11</text><text x="273.2" y="146">12</text><text x="292.9" y="146">13</text><text x="312.6" y="146">14</text><text x="332.3" y="146">15</text>
    <text x="358" y="146">[Stunden]</text>
  </g>
  <text x="195" y="166" font-size="14" fill="#00503c" text-anchor="middle">Wochenstunden</text>
  <rect x="133" y="176" width="16" height="10" fill="var(--turquoise)"/>
  <text x="152" y="184.5" font-size="8.5" fill="#00503c">Preis pro Stunde</text>
  <rect x="133" y="193" width="16" height="10" fill="#00503c"/>
  <text x="152" y="201.5" font-size="8.5" fill="#00503c">Zusätzliche Stunden: + 2 €</text>
</svg>

<section class="panel panel-middle">
  <h2>Die Praxis</h2>
  <div class="copy">
    <p>In unserer Praxis an der Sonnenwiese können Sie frisch renovierte, hochwertig ausgestattete Therapie- und Seminarräume direkt am Sendlinger Tor mieten. Wann und wie lange, das entscheiden Sie, die Zeiten sind flexibel wählbar.</p>
    <p>Neben den einzelnen Therapieräumen bietet Ihnen die Praxis:</p>
    <p style="margin-top:26px">Wartebereich für Patienten,<br>Teeküche (Kühlschrank, Wasserkocher, Kaffemaschine)<br>Kaffee und Tee zum Selbstkostenpreis<br>Wirklich schnelles WLAN (100 mbit/s)<br>Eigenes Schließfach bei Bedarf<br>Eigener Briefkasten bei Bedarf<br>Aufzug in den 6. Stock<br>3 Stufen im Erdgeschoss zum Aufzug</p>
  </div>
  <div class="middle-divider"></div>
  <h2>Impressum</h2>
  <div class="copy">
    <p>Praxis an der Sonnenwiese<br>Helena Korvin-Stahl<br>Lindenweg 22<br>80331 München</p>
    <p>Tel.: 0176 55501234<br>E-Mail: kontakt@praxis-sonnenwiese.de</p>
  </div>
</section>
<div class="photo-bottom-line"></div>
<div class="photo photo-bottom" role="img" aria-label="Foto eines Therapieraums mit zwei grauen Sesseln, kleinem Tisch mit Blumen und Sideboard"></div>

<section class="panel panel-right">
  <div class="brand">
    <div class="brand-mark"></div>
    <div class="brand-name">PRAXIS AN DER<br>SONNENWIESE</div>
  </div>
</section>
<div class="brand-line"></div>
<div class="photo photo-top" role="img" aria-label="Foto eines hellen Therapieraums mit grauem Sessel, Sofa, Couchtisch und Schreibtisch"></div>

<div class="right-bar"></div>
<div class="benefits">
  <p class="intro">Flexible Raummieten im Herzen von München.</p>
  <p>Was wir Ihnen bieten:</p>
</div>

<div class="benefit" style="top:495px">
  <div class="benefit-icon"><svg width="48" height="48" viewBox="0 0 48 48" fill="none" stroke="#111" stroke-width="2" stroke-linejoin="round"><path d="M24 44V8M18 14l6-6 6 6M24 26L8 18M8 18l7-2M8 18l3 6M24 26l16-8M40 18l-7-2M40 18l-3 6"/></svg></div>
  <div class="benefit-text">Höchste Flexibilität durch individuelle Buchungsoptionen</div>
</div>
<div class="benefit" style="top:567px">
  <div class="benefit-icon"><svg width="48" height="48" viewBox="0 0 48 48" fill="none" stroke="#111" stroke-width="2"><circle cx="24" cy="26" r="16"/><path d="M29 19a7 7 0 1 0 0 14M16 24h10M16 28h10"/></svg></div>
  <div class="benefit-text" style="padding-top:18px">Kostenersparnis durch auf Ihren Bedarf zugeschnittene Mietzeiten</div>
</div>
<div class="benefit" style="top:639px">
  <div class="benefit-icon"><svg width="48" height="52" viewBox="0 0 48 52" fill="none" stroke="#111" stroke-width="2"><path d="M24 40C14 28 12 22 12 17a12 12 0 0 1 24 0c0 5-2 11-12 23z"/><circle cx="24" cy="17" r="5"/><ellipse cx="24" cy="44" rx="20" ry="5"/></svg></div>
  <div class="benefit-text" style="padding-top:12px">Gute Anbindungsmöglichkeiten durch zentralen Standort</div>
</div>
<div class="benefit" style="top:711px">
  <div class="benefit-icon"><svg width="50" height="56" viewBox="0 0 50 56" fill="none" stroke="#111" stroke-width="2.5"><path d="M16 38a12 12 0 0 1-4-22 13 13 0 0 1 26 0 12 12 0 0 1-4 22z"/><path d="M25 56V22M25 36l8-7M25 32l-6-5"/></svg></div>
  <div class="benefit-text" style="padding-top:14px">Schöne, idyllische Atmosphäre mit Blick ins Grüne</div>
</div>

</body>
</html>
```